Web Site Design For Real Estate Sales Project

The idea behind this project is pretty simple. I am putting my penthouse apartment up for sale and am trying to be creative in selling it.
Technically this will be pretty simple, it will be 3 pages but graphically this has to be as impressive as possible which is why I am trying Pixel Harbor.
The apartment is located in Barra Da Tijuca, Rio De Janeiro, Brazil. (This is where the 2016 Meridian Regatta will be held)
I am looking for an index page and 2 sub-pages. I am open to all kinds of designs and navigation's but it has to make an impression quickly with a professional and enticing design. The index page should make it obvious that there is a penthouse apartment for sale in Barra Da Tijuca ( suburb of Rio De Janeiro). The first sub page is about the Condominium where the apartment is located, the second sub page is about the apartment itself.
Here is a more detailed description of what the 3 pages should be about.
Index Page
This is the landing page and should make it obvious that there is an apartment for sale in Barra Da Tijuca, Rio De Janeiro with the following attributes
251 SQ M
Duplex Penthouse
4 suites
Price R$ 2.200.000
Price per SQ M: R$ 8.764
First Sub-Page
This is about the Condominium which is called "Gentle Palm Residences" with the following bullets
*Family friendly and safe
*Direct access to the beach
*Many amenities like pool, football court, gym, sauna
There should be some photos of the condominium and a link to the site of the condominium ( www.gprvx.com )
Second Sub-page
This is about the apartment. It should list in bullets the features of the apartment and then have a photo gallery of the view and various rooms. I have attached sample photos but will eventually have to use more photos.
Apartment Features
Price: R$ 2.220.000
251 m2 Duplex Penthouse
4 suites
maids room with bath
guest bathroom
living room
dinning room
Terrace with heated pool for year round use
Veranda
As mentioned above I am open to all designs and navigation so feel free to be creative. The important thing is catch peoples attention and get the message across in a few seconds, which is that there is an apartment for sale at this price with these features in this location. I will then use brightlist promoter and SEO to get people to the site.
Thanks
Target Market(s)
Men and Women from 30-60 years of age.
Industry/Entity Type
Apartment

```html
<!DOCTYPE html>
<html lang="en">
<head>
<meta charset="utf-8">
<title>Lagoa Crest – Apartment for Sale</title>
<link rel="stylesheet" href="https://fonts.googleapis.com/css2?family=Alegreya:wght@500;700&family=Arimo:wght@400;700&display=swap">
<style>
  :root {
    --wall: #e3e3e3;
    --wall-shade: #d6d6d6;
    --brand-red: #a8262b;
    --nav-red: #b3282d;
    --nav-edge: #8e1d22;
    --footer-red: #9c1b20;
    --nav-active: #ffd800;
    --panel: #ffffff;
    --text: #333333;
    --divider: #bdbdbd;
    --photo-sky: #c9d6dc;
    --photo-ground: #9a958c;
    --photo-green: #6f8f5a;
    --photo-pool: #5a9bb5;
    --pin-green: #5aa62c;
  }
  * { box-sizing: border-box; margin: 0; padding: 0; }
  html, body { width: 1200px; height: 687px; overflow: hidden; }
  body {
    position: relative;
    background: radial-gradient(ellipse at center, var(--wall) 0%, var(--wall-shade) 100%);
    font-family: "Arimo", Arial, sans-serif;
    color: var(--text);
  }

  .brand {
    position: absolute; top: 12px; left: 0; width: 1200px;
    display: flex; justify-content: center; align-items: center; gap: 14px;
  }
  .brand-mark { width: 22px; height: 22px; background: var(--brand-red); }
  .brand-name {
    font-family: "Alegreya", Georgia, serif; font-weight: 700;
    font-size: 38px; color: var(--brand-red); line-height: 1;
  }

  .main-nav {
    position: absolute; left: 350px; top: 72px; width: 510px; height: 54px;
    background: var(--nav-red); border: 1px solid var(--nav-edge);
    box-shadow: inset 0 0 0 4px var(--nav-red), inset 0 0 0 5px rgba(255,255,255,0.18);
  }
  .main-nav ul { list-style: none; display: flex; height: 100%; padding-left: 14px; padding-top: 17px; }
  .main-nav li { padding: 0 16px; border-left: 1px solid rgba(255,255,255,0.22); height: 24px; }
  .main-nav li:first-child { border-left: none; }
  .main-nav a { color: #fff; text-decoration: none; font-size: 13px; }
  .main-nav a.is-active { color: var(--nav-active); text-decoration: underline; }

  .content-panel {
    position: absolute; left: 205px; top: 121px; width: 791px; height: 474px;
    background: var(--panel);
    box-shadow: 0 22px 26px -14px rgba(0,0,0,0.45);
  }
  .hero-photo {
    position: absolute; left: 8px; top: 9px; width: 597px; height: 325px;
    background: linear-gradient(180deg, var(--photo-sky) 0%, #b7c0bd 35%, var(--photo-green) 48%, var(--photo-ground) 70%, #b8b2a6 100%);
  }
  .thumb { position: absolute; left: 617px; width: 164px; height: 96px; }
  .thumb-entrance { top: 9px; background: linear-gradient(180deg, #8a5a4a 0%, #9d8f80 50%, #6f8a55 100%); }
  .thumb-pool { top: 123px; background: linear-gradient(180deg, #7d8a5c 0%, var(--photo-pool) 50%, #9b8d6e 100%); }
  .thumb-street { top: 237px; background: linear-gradient(180deg, #9fc0dc 0%, #a8775e 45%, #8f8f8f 100%); }

  .info-row { position: absolute; left: 0; top: 343px; width: 791px; height: 120px; }
  .col-divider { position: absolute; top: 0; width: 1px; height: 118px; background: var(--divider); }

  .sale-icon { position: absolute; left: 10px; top: 4px; }
  .sale-title {
    position: absolute; left: 83px; top: 4px;
    font-family: "Alegreya", Georgia, serif; font-weight: 700; font-size: 22px; color: #222;
  }
  .sale-price { position: absolute; left: 83px; top: 32px; font-size: 26px; color: var(--brand-red); }
  .sale-note { position: absolute; left: 10px; top: 72px; width: 275px; font-size: 12.5px; line-height: 1.3; }

  .location-pin { position: absolute; left: 320px; top: 8px; }
  .location-text { position: absolute; left: 355px; top: 8px; width: 240px; font-size: 12px; line-height: 1.25; }
  .spec-list { position: absolute; left: 320px; top: 53px; list-style: none; font-size: 12.5px; line-height: 1.2; }
  .spec-list strong { font-weight: 700; }

  .contact-phone-icon { position: absolute; left: 617px; top: 26px; }
  .contact-phone { position: absolute; left: 650px; top: 25px; font-size: 22px; font-weight: 700; color: var(--brand-red); }
  .contact-email { position: absolute; left: 617px; top: 59px; font-size: 13px; font-weight: 700; color: var(--footer-red); }

  .site-footer {
    position: absolute; left: 451px; top: 595px; width: 300px; height: 56px;
    background: var(--footer-red);
    box-shadow: inset 0 0 0 6px var(--footer-red), inset 0 0 0 7px rgba(255,255,255,0.2);
    color: #fff; font-size: 11px; text-align: center; padding-top: 14px;
  }
  .site-footer strong { font-size: 14px; }
</style>
</head>
<body>
  <header class="brand">
    <span class="brand-mark"></span>
    <span class="brand-name">Lagoa Crest</span>
  </header>

  <nav class="main-nav">
    <ul>
      <li><a class="is-active" href="#">Home</a></li>
      <li><a href="#">Gentle Palm Residences</a></li>
      <li><a href="#">About the Apartment</a></li>
      <li><a href="#">Contact Us</a></li>
    </ul>
  </nav>

  <main class="content-panel">
    <div class="hero-photo" role="img" aria-label="Condominium terrace with white tables, chairs and large grey parasols beside palm trees"></div>
    <div class="thumb thumb-entrance" role="img" aria-label="Condominium entrance gate with gardens"></div>
    <div class="thumb thumb-pool" role="img" aria-label="Condominium swimming pool seen from above"></div>
    <div class="thumb thumb-street" role="img" aria-label="Residential towers along the street"></div>

    <section class="info-row">
      <svg class="sale-icon" width="60" height="60" viewBox="0 0 60 60" aria-hidden="true">
        <polygon points="6,28 30,8 54,28" fill="#4f6f95"/>
        <rect x="12" y="28" width="36" height="26" fill="#f2f2f2" stroke="#999"/>
        <rect x="26" y="38" width="9" height="16" fill="#4f6f95"/>
        <rect x="16" y="33" width="7" height="7" fill="#9cc3e0"/>
      </svg>
      <h1 class="sale-title">Apartment for Sale</h1>
      <p class="sale-price">R$ 2.200.000</p>
      <p class="sale-note">The apartment is located in Barra Da Tijuca, Rio De Janeiro, Brazil. (This is where the 2016 Meridian Regatta will be held)</p>

      <span class="col-divider" style="left:292px"></span>

      <svg class="location-pin" width="22" height="32" viewBox="0 0 22 32" aria-hidden="true">
        <path d="M11 1C5.5 1 1 5.5 1 11c0 7.5 10 20 10 20s10-12.5 10-20C21 5.5 16.5 1 11 1z" fill="var(--pin-green)"/>
        <circle cx="11" cy="11" r="4" fill="#2b2b2b"/>
      </svg>
      <p class="location-text">Barra Da Tijuca, Rio De Janeiro with the following attributes</p>
      <ul class="spec-list">
        <li><strong>Building Size</strong> : 251 SQ M</li>
        <li><strong>Property Type :</strong> Duplex Penthouse</li>
        <li><strong>No. of Suites :</strong> 4 suites</li>
        <li><strong>Price per SQ M :</strong> R$ 8.764</li>
      </ul>

      <span class="col-divider" style="left:602px"></span>

      <svg class="contact-phone-icon" width="24" height="20" viewBox="0 0 24 20" aria-hidden="true">
        <path d="M2 7c0-4 20-4 20 0v2h-5V6H7v3H2z" fill="#333"/>
        <path d="M6 9h12l3 9H3z" fill="#333"/>
        <circle cx="12" cy="13.5" r="2.5" fill="#fff"/>
      </svg>
      <p class="contact-phone">555 210 384</p>
      <p class="contact-email">Info@lagoa-crest.com</p>
    </section>
  </main>

  <footer class="site-footer">
    <strong>Lagoa Crest</strong> © 2013. All Right Reserved.
  </footer>
</body>
</html>
```